I am a surgeon that operates on gynaecological cancer. Wish a design and logo for letter head.

Design should include my name: Dr. Kiran Mudaly, qualifications: FTELSWOB, CGO. and state that I am a Gynaecological Oncologist and Advanced Laparoscopic Surgeon.
As for a logo. As all cancer is related to DNA, I think that that double helix could be used to symbolise a female shape, exaggerating the abdomen to suggest a mass.

Reason: Extended to view changes I have asked for.

```html
<!DOCTYPE html>
<html lang="en">
<head>
<meta charset="utf-8">
<title>Dr. Kiran Mudaly – Letterhead</title>
<link href="https://fonts.googleapis.com/css2?family=EB+Garamond:wght@400&family=Arimo:wght@400&display=swap" rel="stylesheet">
<style>
  :root {
    --backdrop: #e6e7e9;
    --paper: #ffffff;
    --band-light: #bccbd4;
    --band-dark: #8aa0ab;
    --ink-white: #ffffff;
    --ink-grey: #8e9396;
    --mark-faint: #f1f2f2;
  }
  html, body {
    margin: 0;
    padding: 0;
    width: 1200px;
    height: 1000px;
    overflow: hidden;
    background: var(--backdrop);
  }
  .letterhead {
    position: absolute;
    left: 343px;
    top: 136px;
    width: 515px;
    height: 728px;
    background: var(--paper);
  }
  .header-band {
    position: absolute;
    left: 0;
    top: 41px;
    width: 515px;
    height: 59px;
    background: linear-gradient(to right, var(--band-light) 0, var(--band-light) 254px, var(--band-dark) 254px, var(--band-dark) 100%);
  }
  .doctor-name {
    position: absolute;
    left: 305px;
    top: 49px;
    margin: 0;
    font-family: "EB Garamond", Georgia, serif;
    font-weight: 400;
    font-size: 24px;
    line-height: 1;
    color: var(--ink-white);
    white-space: nowrap;
  }
  .qualifications {
    position: absolute;
    right: 37px;
    top: 80px;
    margin: 0;
    font-family: "Arimo", Arial, sans-serif;
    font-size: 8.5px;
    line-height: 1;
    color: var(--ink-white);
    letter-spacing: 0.2px;
  }
  .speciality {
    position: absolute;
    left: 305px;
    top: 104px;
    margin: 0;
    font-family: "EB Garamond", Georgia, serif;
    font-size: 11px;
    line-height: 16px;
    color: var(--ink-grey);
  }
  .speciality .line-spaced {
    display: block;
    letter-spacing: 2.1px;
  }
  .speciality .line-plain {
    display: block;
    letter-spacing: 0;
  }
  .faint-mark {
    position: absolute;
    left: 0;
    width: 515px;
    top: 400px;
    margin: 0;
    text-align: center;
    font-family: "EB Garamond", Georgia, serif;
    font-size: 40px;
    line-height: 1;
    color: var(--mark-faint);
  }
</style>
</head>
<body>
  <main class="letterhead">
    <div class="header-band"></div>
    <h1 class="doctor-name">Dr. Kiran Mudaly</h1>
    <p class="qualifications">FTELSWOB, CGO.</p>
    <p class="speciality">
      <span class="line-spaced">Gynaecological Oncologist</span>
      <span class="line-plain">and Advanced Laparoscopic Surgeon</span>
    </p>
    <p class="faint-mark" aria-hidden="true">Kiran Mudaly</p>
  </main>
</body>
</html>
```